Display ads - Med spa Velmira promotion

Please create an ad creative for a promotional special for a med spa:
First-time customers who book a Velmira appointment receive $50 off the Velmira treatment

Please have an aspect of diversity in the ad (the company is black and woman-owned, so more than just white people in the ad creative

The company goes for "clean and tranquil" as part of their aesthetic

Attached here are the logo and picture of the homepage, and other images on the website, typical of the aesthetic of the company identity

you can find the website here for inspiration: thedewlinestudioct.com

Please no "black and white" photography, full color only, thank you!

Target Market(s)

New Haven, Connecticut, wealthy individuals who want to look and feel younger, want great skin, and want to feel youthful

Industry/Entity Type

Medspa/beauty

Requirements
Must have
• Need 5 sizes that fit the following Medium rectangle: 300×250; Large rectangle: 300×600 ; 728x90, 300x50; 160x600
Nice to have
• Clean, refined, bright
Should not have
• black and white photos, cartoonish, or drawn items

```html
<!DOCTYPE html>
<html lang="en">
<head>
<meta charset="utf-8">
<title>Velmira First-Time Offer</title>
<link href="https://fonts.googleapis.com/css2?family=Poppins:wght@400;500;600;700;800&display=swap" rel="stylesheet">
<style>
  :root {
    --bg-light: #ecbf92;
    --bg-deep: #d99a60;
    --frame: #f8d8b6;
    --panel-light: #eebd8a;
    --panel-deep: #cf8d4c;
    --white: #ffffff;
    --rust: #a83200;
    --cream: #fffbd0;
    --hair-dark: #3a2114;
    --hair-mid: #6e4126;
    --skin-deep: #8a4f2e;
    --skin-warm: #b5714a;
    --skin-glow: #d79b6e;
  }
  html, body {
    margin: 0;
    padding: 0;
    width: 1200px;
    height: 1000px;
    overflow: hidden;
  }
  body {
    font-family: "Poppins", sans-serif;
  }
  .ad {
    position: relative;
    width: 1200px;
    height: 1000px;
    overflow: hidden;
    background: linear-gradient(135deg, var(--bg-light) 0%, var(--bg-deep) 100%);
  }
  .offer-frame {
    position: absolute;
    left: 446px;
    top: 66px;
    width: 690px;
    height: 862px;
    box-sizing: border-box;
    border: 22px solid var(--frame);
    background: radial-gradient(circle at 45% 50%, var(--panel-light) 0%, var(--panel-deep) 100%);
  }
  .hero-photo {
    position: absolute;
    left: 0;
    top: 0;
    width: 600px;
    height: 1000px;
    background:
      radial-gradient(ellipse 62% 34% at 42% 20%, var(--hair-dark) 0%, var(--hair-mid) 55%, rgba(110,65,38,0) 100%),
      radial-gradient(ellipse 40% 30% at 30% 48%, var(--skin-glow) 0%, var(--skin-warm) 70%, rgba(181,113,74,0) 100%),
      linear-gradient(180deg, var(--hair-mid) 0%, var(--skin-deep) 45%, var(--skin-warm) 75%, var(--skin-deep) 100%);
    border-top-right-radius: 300px 360px;
    -webkit-mask-image: linear-gradient(90deg, #000 80%, rgba(0,0,0,0) 100%);
    mask-image: linear-gradient(90deg, #000 80%, rgba(0,0,0,0) 100%);
  }
  .headline-line {
    position: absolute;
    right: 110px;
    margin: 0;
    line-height: 1;
    white-space: nowrap;
    text-align: right;
  }
  .line-first     { top: 168px; font-size: 92px;  font-weight: 400; color: var(--white); letter-spacing: -1px; }
  .line-customers { top: 256px; font-size: 64px;  font-weight: 400; color: var(--white); letter-spacing: -0.5px; }
  .line-book      { top: 322px; font-size: 60px;  font-weight: 600; color: var(--white); letter-spacing: -0.5px; }
  .line-appoint   { top: 393px; font-size: 50px;  font-weight: 400; color: var(--rust); letter-spacing: -2px; }
  .line-price     { top: 435px; font-size: 168px; font-weight: 800; color: var(--rust); letter-spacing: -7px; }
  .line-the       { top: 594px; font-size: 96px;  font-weight: 600; color: var(--cream); letter-spacing: -1px; }
  .line-treatment { top: 677px; font-size: 74px;  font-weight: 600; color: var(--cream); letter-spacing: -0.5px; }
  .book-button {
    position: absolute;
    left: 774px;
    top: 810px;
    width: 312px;
    height: 54px;
    border-radius: 27px;
    background: var(--rust);
    color: var(--white);
    font-size: 29px;
    font-weight: 700;
    display: flex;
    align-items: center;
    justify-content: center;
    text-decoration: none;
  }
</style>
</head>
<body>
  <div class="ad">
    <div class="offer-frame"></div>
    <div class="hero-photo" role="img" aria-label="Full-colour portrait of a smiling Black woman with voluminous curly natural hair, eyes closed, hand resting on her shoulder, in warm golden light"></div>
    <p class="headline-line line-first">First-time</p>
    <p class="headline-line line-customers">customers who</p>
    <p class="headline-line line-book">book a Velmira</p>
    <p class="headline-line line-appoint">appointment receive</p>
    <p class="headline-line line-price">$50 off</p>
    <p class="headline-line line-the">the Velmira</p>
    <p class="headline-line line-treatment">treatment</p>
    <a class="book-button" href="#">BOOK NOW</a>
  </div>
</body>
</html>
```